Marlow Crest Group (Real Estate and Investment)

A high end, clean design.
We are a real estate company with sales, asset management and investment divisions. We want to use a black and white scheme which is really high end feel. The back of the card can just be the logo (black background with the white writing) as we will probably emboss this when we print)

Target Market(s)

High level investors, high end houses for sale

Industry/Entity Type

Business

Contact Information for Business Card

Name, position, phone number and email address
Glen Varley, Managing Director, 0437259064 and glen@marlowcrest-example.com.au

Requirements
Must have
• Back of the card to be the black background with the white writing (as per the attached images). Would like the capacity to emboss the writing and logo

```html
<!DOCTYPE html>
<html lang="en">
<head>
<meta charset="utf-8">
<title>Marlow Crest Group – Business Card</title>
<link href="https://fonts.googleapis.com/css2?family=Inter:wght@500&family=Open+Sans:wght@400;600&display=swap" rel="stylesheet">
<style>
  :root {
    --page-bg: #e9e6e2;
    --card-top: #f7f6f4;
    --card-bottom: #e4e2df;
    --card-edge: #c9c6c2;
    --ink: #1f1d1d;
    --band-text: #d9d1d0;
    --band-name: #e6e1df;
  }
  html, body {
    margin: 0;
    width: 1200px;
    height: 1200px;
    overflow: hidden;
    background: var(--page-bg);
  }
  .card {
    position: absolute;
    left: 60px;
    top: 300px;
    width: 1080px;
    height: 600px;
    background: linear-gradient(160deg, var(--card-top), var(--card-bottom));
    border: 1px solid var(--card-edge);
    box-sizing: border-box;
    overflow: hidden;
  }
  .brand-mark {
    position: absolute;
    left: 0;
    top: 0;
  }
  .brand-name {
    position: absolute;
    left: 50px;
    top: 198px;
    width: 330px;
    margin: 0;
    text-align: center;
    font-family: "Inter", sans-serif;
    font-weight: 500;
    font-size: 36px;
    line-height: 44px;
    letter-spacing: -0.6px;
    color: var(--ink);
    white-space: nowrap;
  }
  .band {
    position: absolute;
    left: 0;
    top: 324px;
    width: 1080px;
    height: 246px;
  }
  .contact {
    position: absolute;
    left: 50px;
    top: 348px;
    font-family: "Open Sans", sans-serif;
    color: var(--band-text);
  }
  .contact-name {
    margin: 0;
    font-weight: 600;
    font-size: 36px;
    line-height: 1.1;
    color: var(--band-name);
  }
  .contact-role {
    margin: 2px 0 0;
    font-size: 24px;
    line-height: 1.2;
  }
  .contact-list {
    list-style: none;
    margin: 24px 0 0;
    padding: 0;
    font-size: 24px;
    line-height: 33px;
  }
  .contact-list li {
    display: flex;
    align-items: center;
    gap: 14px;
  }
  .contact-list svg {
    width: 22px;
    height: 22px;
    flex: none;
  }
  .emblem-ring {
    position: absolute;
    left: 0;
    top: 0;
  }
</style>
</head>
<body>
  <div class="card">
    <svg class="brand-mark" width="1080" height="600" aria-hidden="true">
      <circle cx="215" cy="115" r="62" fill="none" stroke="var(--ink)" stroke-width="2.5"/>
    </svg>
    <p class="brand-name">Marlow Crest Group</p>

    <svg class="band" viewBox="0 0 1080 246" aria-hidden="true">
      <defs>
        <linearGradient id="bandShade" x1="0" y1="0" x2="1" y2="0">
          <stop offset="0" stop-color="#2b292a"/>
          <stop offset="0.55" stop-color="#151415"/>
          <stop offset="1" stop-color="#0a0a0a"/>
        </linearGradient>
        <mask id="bandCut">
          <rect width="1080" height="246" fill="#fff"/>
          <circle cx="894" cy="123" r="136" fill="#000"/>
        </mask>
      </defs>
      <rect width="900" height="246" fill="url(#bandShade)" mask="url(#bandCut)"/>
    </svg>

    <svg class="emblem-ring" width="1080" height="600" aria-hidden="true">
      <circle cx="894" cy="447" r="124" fill="none" stroke="var(--ink)" stroke-width="3"/>
    </svg>

    <div class="contact">
      <p class="contact-name">Glen Varley</p>
      <p class="contact-role">Managing Director</p>
      <ul class="contact-list">
        <li>
          <svg viewBox="0 0 24 24"><path fill="currentColor" d="M6.6 10.8a15.1 15.1 0 0 0 6.6 6.6l2.2-2.2a1 1 0 0 1 1-.25 11.4 11.4 0 0 0 3.6.57 1 1 0 0 1 1 1V20a1 1 0 0 1-1 1A17 17 0 0 1 3 4a1 1 0 0 1 1-1h3.5a1 1 0 0 1 1 1c0 1.25.2 2.45.57 3.57a1 1 0 0 1-.25 1z"/></svg>
          <span>0437259064</span>
        </li>
        <li>
          <svg viewBox="0 0 24 24"><rect x="2" y="5" width="20" height="14" fill="currentColor"/><path d="M2 5l10 8 10-8" fill="none" stroke="#151415" stroke-width="2"/></svg>
          <span>glen@marlowcrest-example.com.au</span>
        </li>
        <li>
          <svg viewBox="0 0 24 24"><circle cx="12" cy="12" r="9" fill="none" stroke="currentColor" stroke-width="2"/><path d="M3 12h18M12 3c3 3 3 15 0 18M12 3c-3 3-3 15 0 18" fill="none" stroke="currentColor" stroke-width="1.5"/></svg>
          <span>www.marlowcrest-example.com.au</span>
        </li>
      </ul>
    </div>
  </div>
</body>
</html>
```